TallyNest Webpages and Logo

See attached brief. Take the existing website www.tallynest.co.uk and logo and transform these assets to:

Give people who arrive on the site for first time the confidence to sign-up easily and quickly
Allow regular returning users quick and easy placing of predictions and encourage them to share the TallyNest prediction on social networks and with their contacts
Convey the essence of a community working together to enjoyably come-up with smart predictions on sporting events
Work seamlessly and well across smartphones, tablets and desktop i.e. Should be Responsive Web Design
Updates

Target Market(s)

Users are sports fans with opinions
Primarily male and early twenties to mid-thirties
They are competitive - they want to beat their peers
Many are from outside the UK

Industry/Entity Type

Events

Logo Text

TallyNest

Coding

Coded - Design and coding required

Number of Pages Required

4 page

Font styles to use
Sans Serif

Requirements
Must have
• Responsive Web Design
• Mobile First
• HTML must work with dedicated bespoke application developed in ASP.NET using MS SQL underneath
• See Brief
Nice to have
• See brief
Should not have
• See brief

```html
<!DOCTYPE html>
<html lang="en">
<head>
<meta charset="utf-8">
<title>TallyNest – Home</title>
<link rel="stylesheet" href="https://fonts.googleapis.com/css2?family=Varela+Round&family=Roboto:wght@400;500&display=swap">
<style>
  :root{
    --ink:#333;
    --muted:#555;
    --green:#129a12;
    --green-soft:#effbef;
    --blue-soft:#a2bfde;
    --panel:#f2f2f2;
    --header:#f4f4f4;
    --dark-btn:#4a4a4a;
    --footer:#3a3a3a;
    --footer-text:#bdbdbd;
    --red-dot:#e03b2e;
  }
  *{box-sizing:border-box;margin:0;padding:0}
  html,body{width:1074px;height:1200px;overflow:hidden;background:#fff;font-family:"Varela Round",sans-serif;color:var(--ink)}
  .page{position:relative;width:1074px;height:1200px}
  .abs{position:absolute}

  .site-header{position:absolute;left:0;top:0;width:1074px;height:97px;background:var(--header)}
  .brand{left:117px;top:33px;font-size:34px;letter-spacing:.5px;color:#555;display:flex;align-items:center;gap:8px}
  .brand-dot{width:14px;height:14px;border-radius:50%;background:var(--green)}
  .kitty{left:853px;top:29px;font-size:12.5px;color:#333;display:flex;gap:8px;align-items:center}
  .kitty .rise{color:var(--green)}
  .nav a{position:absolute;top:74px;font-size:13px;color:#555;text-decoration:none}
  .nav a.active{color:var(--green)}
  .nav-underline{left:543px;top:94px;width:54px;height:3px;background:var(--green)}

  .promo{left:116px;top:117px;width:842px;height:88px;background:var(--green-soft)}
  .promo p{position:absolute;left:19px;font-size:12.5px;color:#444}
  .join{left:740px;top:145px;width:192px;height:35px;background:var(--green);color:#fff;font-size:13px;display:flex;align-items:center;justify-content:center}

  .hero{left:116px;top:223px;width:842px;height:345px;background:linear-gradient(180deg,#f97c5e 0%,#f9955c 35%,#f8b85a 55%,#1a1a1a 72%,#050505 100%)}
  .hero-bar{left:153px;top:455px;width:541px;height:43px;background:rgba(90,70,40,.75);display:flex;align-items:center;padding-left:16px;gap:40px}
  .hero-bar h2{font-size:22px;color:#fff;font-weight:400}
  .share{display:flex;gap:6px;align-items:center;font-family:Roboto,sans-serif;font-size:11px}
  .share .btn{background:#4a6bb0;color:#fff;padding:2px 6px;border-radius:2px}
  .share .btn.alt{background:#3aa0e0}
  .share .count{background:#fff;color:#333;padding:2px 4px;border:1px solid #ccc;border-radius:2px}
  .dots{left:513px;top:581px;display:flex;gap:6px}
  .dots span{width:8px;height:8px;border-radius:50%;background:#d8d8d8}
  .dots span.on{background:var(--red-dot)}

  .stat{top:639px;height:142px;background:var(--panel);text-align:center}
  .stat h3{height:46px;background:var(--blue-soft);font-weight:400;font-size:16px;line-height:46px;color:#222}
  .stat p{font-size:16px;color:#333;padding:26px 24px 0;line-height:1.45}

  .section-title{left:0;width:1074px;top:836px;text-align:center;font-size:22px;color:var(--green)}
  .title-rule{left:420px;top:866px;width:228px;height:2px;background:#ddd}

  .match{top:905px;width:214px;text-align:center;font-family:Roboto,sans-serif}
  .teams{display:flex;justify-content:center;align-items:flex-start;gap:6px;height:86px}
  .team{width:90px;font-size:11px;color:#333;line-height:1.2}
  .crest{display:block;margin:2px auto 8px;width:36px;height:40px}
  .vs{font-size:12px;padding-top:26px;color:#333}
  .kickoff{font-size:13px;color:#444;margin-top:2px}
  .predict{display:block;width:147px;height:30px;margin:10px auto 0;background:var(--dark-btn);color:#fff;font-size:13px;line-height:30px}
  .predict.primary{background:var(--green)}

  .site-footer{left:0;top:1103px;width:1074px;height:97px;background:var(--footer);font-family:Roboto,sans-serif}
  .footer-links{position:absolute;left:120px;top:28px;display:flex;gap:15px;font-size:12px;color:var(--footer-text)}
  .copyright{position:absolute;left:120px;top:58px;font-size:11.5px;color:var(--footer-text)}
  .social{position:absolute;left:846px;top:40px;display:flex;gap:6px}
  .social span{width:23px;height:23px;border-radius:3px}
</style>
</head>
<body>
<div class="page">
  <header class="site-header">
    <div class="abs brand"><span>TALLYNEST</span><span class="brand-dot"></span></div>
    <div class="abs kitty"><span>kitty:£1289</span><span class="rise">↑ <span style="color:#333">3%</span></span></div>
    <nav class="nav">
      <a class="active" style="left:552px">Home</a>
      <a style="left:624px">MiniLiga</a>
      <a style="left:720px">Tables</a>
      <a style="left:804px">Kitty</a>
      <a style="left:873px">FAQ</a>
      <a style="left:938px">Me</a>
    </nav>
    <div class="abs nav-underline"></div>
  </header>

  <section class="abs promo">
    <p style="top:24px">Predict results, scores and scorers for your free chance to win a £20 Marketly voucher every week.</p>
    <p style="top:48px">Overall season winner gets up to £1000 in Marketly vouchers! No entry fee and no catches.</p>
  </section>
  <div class="abs join">JOIN NOW</div>

  <div class="abs hero" role="img" aria-label="Silhouetted crowd of fans cheering with raised arms against an orange sunset sky"></div>
  <div class="abs hero-bar">
    <h2>TALLYNEST HOT TIPS!</h2>
    <div class="share">
      <span class="btn">Share</span><span class="count">60k</span>
      <span style="width:10px"></span>
      <span class="btn alt">Tweet</span><span class="count">7,231</span>
    </div>
  </div>
  <div class="abs dots"><span class="on"></span><span></span><span></span><span></span></div>

  <div class="abs stat" style="left:116px;width:276px"><h3>RESULT&nbsp; 100%</h3><p>WEST HOLM UNITED WIN</p></div>
  <div class="abs stat" style="left:396px;width:282px"><h3>SCORE 42%</h3><p style="padding-top:24px">ASHFORD VALE 0 NORTHGATE UNITED 2</p></div>
  <div class="abs stat" style="left:682px;width:276px"><h3>1st GOAL&nbsp;&nbsp;&nbsp; 50%</h3><p>van Dorsten R</p></div>

  <h2 class="abs section-title" style="font-weight:400">PREDICT SOCRE</h2>
  <div class="abs title-rule"></div>

  <div class="abs match" style="left:102px">
    <div class="teams">
      <div class="team"><svg class="crest" viewBox="0 0 36 40"><rect x="4" y="4" width="28" height="32" rx="4" fill="#7ab0d8"/></svg>Northgate City</div>
      <div class="vs">v</div>
      <div class="team"><svg class="crest" viewBox="0 0 36 40"><circle cx="18" cy="20" r="16" fill="#3156a3"/></svg>Glass Harbour</div>
    </div>
    <div class="kickoff">Sat 20 Dec 2014 - 12:45 PM</div>
    <span class="predict primary">Predict Score Now</span>
  </div>
  <div class="abs match" style="left:324px">
    <div class="teams">
      <div class="team"><svg class="crest" viewBox="0 0 36 40"><rect x="4" y="2" width="28" height="34" rx="4" fill="#7a9ad0"/></svg>Ashford Vale</div>
      <div class="vs">v</div>
      <div class="team"><svg class="crest" viewBox="0 0 36 40"><circle cx="18" cy="20" r="17" fill="#d8281e"/></svg>Northgate United</div>
    </div>
    <div class="kickoff">Sat 20 Dec 2014 - 12:45 PM</div>
    <span class="predict">Predict Score Now</span>
  </div>
  <div class="abs match" style="left:538px">
    <div class="teams">
      <div class="team"><svg class="crest" viewBox="0 0 36 40"><circle cx="18" cy="20" r="16" fill="#2d5aa8"/></svg>Kings Meadow Rangers</div>
      <div class="vs">v</div>
      <div class="team"><svg class="crest" viewBox="0 0 36 40"><rect x="5" y="3" width="26" height="34" rx="4" fill="#1f3f8a"/></svg>Westbrook Albion</div>
    </div>
    <div class="kickoff">Sat 20 Dec 2014 - 12:45 PM</div>
    <span class="predict">Predict Score Now</span>
  </div>
  <div class="abs match" style="left:760px">
    <div class="teams">
      <div class="team"><svg class="crest" viewBox="0 0 36 40"><rect x="10" y="2" width="16" height="36" rx="6" fill="#1c2a5c"/></svg>Thornbury Hotspur</div>
      <div class="vs">v</div>
      <div class="team"><svg class="crest" viewBox="0 0 36 40"><rect x="4" y="3" width="28" height="32" rx="4" fill="#7fb6e0"/></svg>Barnley</div>
    </div>
    <div class="kickoff">Sat 20 Dec 2014 - 12:45 PM</div>
    <span class="predict">Predict Score Now</span>
  </div>

  <footer class="abs site-footer">
    <div class="footer-links"><span>About</span><span>Terms</span><span>Site Map</span><span>Privacy</span><span>Contact Us</span></div>
    <div class="copyright">©2014. Yoursite. Allright reserved.</div>
    <div class="social">
      <span style="background:#f08a2c"></span>
      <span style="background:#3b5ea8"></span>
      <span style="background:#3ba3e3"></span>
      <span style="background:#1a7bb8"></span>
    </div>
  </footer>
</div>
</body>
</html>
```